HOME IMPROVEMENT Business Card

I want a very unique business card. nothing typical and boring. Im open to you ideas. Ive seen cards with gold and silver or color foil and spot UV coatings. Im looking for something that looks cool and grabs attention. I like rounded corners but am open to all suggestions. We are a home improvement company and I will have a presentation folder printed and a catalog printed also and want to keep that same theme. I love the colors in our logo but I am open at looking at a 3rd color that would work with my logo. I hope that helps.
Card should include
Address
Phone
Fax
Email
Website
Target Market(s)
Home owners, people looking to remodel their home
Industry/Entity Type
Home Improvement
Contact Information for Business Card
2873 Maple Crest Avenue Unit 410
Oakridge, IN 60284
Phone
Direct Line
Email
Website
Font styles to use
Other font styles liked:
- IM OPEN MINDED
Requirements
Must have
- High end quality look nothing boring I like rounded corners but am open minded
Nice to have
- WOW. I want something nice and impressive.
Should not have
- ??? Not sure

```html
<!DOCTYPE html>
<html lang="en">
<head>
<meta charset="utf-8">
<title>Keystone – Business Card</title>
<link href="https://fonts.googleapis.com/css2?family=Mulish:wght@400;500;700;800&display=swap" rel="stylesheet">
<style>
  :root {
    --navy: #272844;
    --green: #17953f;
    --paper: #ffffff;
    --paper-shade: #eeeeee;
    --backdrop: #d9dbe0;
    --ink: #2b2c47;
  }
  * { margin: 0; padding: 0; box-sizing: border-box; }
  html, body { width: 1200px; height: 900px; overflow: hidden; }
  body {
    background: var(--backdrop);
    font-family: "Mulish", Arial, sans-serif;
    display: flex; flex-direction: column; align-items: center; justify-content: center;
    gap: 40px;
  }
  .card {
    position: relative;
    width: 640px; height: 366px;
    border-radius: 14px;
    overflow: hidden;
    box-shadow: 0 10px 30px rgba(30, 32, 60, .18);
  }
  .card-front { background: linear-gradient(160deg, var(--paper-shade), var(--paper) 55%); }
  .card-back { background: var(--navy); display: flex; align-items: center; justify-content: center; }

  .front-shapes { position: absolute; inset: 0; }

  .brand { position: absolute; display: flex; align-items: center; gap: 10px; }
  .brand-mark { width: 14px; height: 14px; background: var(--green); }
  .brand-name { font-weight: 800; font-size: 46px; line-height: 1; letter-spacing: -.5px; }
  .card-front .brand { top: 60px; right: 60px; }
  .card-front .brand-name { color: var(--navy); }
  .card-back .brand { position: static; transform: scale(1.25); }
  .card-back .brand-name { color: #ffffff; }

  .person { position: absolute; left: 48px; top: 166px; }
  .person-name { color: var(--green); font-weight: 800; font-size: 27px; line-height: 1.1; }
  .person-role { color: var(--ink); font-weight: 500; font-size: 18px; margin-top: 2px; }

  .contacts { position: absolute; left: 48px; top: 244px; list-style: none; }
  .contacts li { display: flex; align-items: center; gap: 10px; color: var(--ink); font-size: 16.5px; font-weight: 500; height: 24px; }
  .contact-icon { width: 18px; height: 18px; flex: none; }

  .address { position: absolute; right: 48px; top: 198px; text-align: right; color: var(--ink); font-size: 17px; font-weight: 500; font-style: normal; line-height: 1.35; }
  .website { position: absolute; right: 40px; bottom: 12px; color: #ffffff; font-size: 15px; font-weight: 500; letter-spacing: .5px; }
</style>
</head>
<body>
  <section class="card card-front">
    <svg class="front-shapes" width="640" height="366" viewBox="0 0 640 366" aria-hidden="true">
      <line x1="262" y1="176" x2="592" y2="124" stroke="var(--green)" stroke-width="1"/>
      <path d="M0 350 L318 350 L338 318 L640 318 L640 366 L0 366 Z" fill="var(--navy)"/>
      <path d="M0 342 L314 342 L334 310 L346 310 L326 350 L0 350 Z" fill="var(--green)"/>
    </svg>

    <div class="brand">
      <span class="brand-mark"></span>
      <span class="brand-name">Keystone</span>
    </div>

    <div class="person">
      <div class="person-name">Dale Morrison</div>
      <div class="person-role">Operations Manager</div>
    </div>

    <ul class="contacts">
      <li>
        <svg class="contact-icon" viewBox="0 0 18 18" aria-label="Mobile"><circle cx="9" cy="9" r="9" fill="var(--green)"/><rect x="6" y="3.5" width="6" height="11" rx="1.2" fill="none" stroke="#fff" stroke-width="1.4"/><circle cx="9" cy="12.3" r=".8" fill="#fff"/></svg>
        0412 586 204
      </li>
      <li>
        <svg class="contact-icon" viewBox="0 0 18 18" aria-label="Phone"><circle cx="9" cy="9" r="9" fill="var(--green)"/><path d="M5.5 4.5 L7.5 4.5 L8.3 7 L7 8 Q8 10.3 10 11 L11 9.7 L13.5 10.5 L13.5 12.5 Q8.5 13.5 5.5 7.5 Z" fill="#fff"/></svg>
        0412 586 205
      </li>
      <li>
        <svg class="contact-icon" viewBox="0 0 18 18" aria-label="Email"><circle cx="9" cy="9" r="9" fill="var(--green)"/><rect x="4.5" y="5.8" width="9" height="6.4" fill="#fff"/><path d="M4.5 5.8 L9 9.3 L13.5 5.8" fill="none" stroke="var(--green)" stroke-width="1"/></svg>
        dale@keystonehomes.com
      </li>
    </ul>

    <address class="address">
      2873 Maple Crest Avenue Unit 410<br>
      Oakridge, IN 60284
    </address>

    <div class="website">www.keystonehomes.com</div>
  </section>

  <section class="card card-back">
    <div class="brand">
      <span class="brand-mark"></span>
      <span class="brand-name">Keystone</span>
    </div>
  </section>
</body>
</html>
```